Juice bottle label

I need a juice bottle label for a line of cold pressed bottle juices.

Industry/Entity Type

Food Service

Requirements
Must have
• Editable file in adobe illustrator
• Should contain the following warning:
• WARNING: This product has not been pasteurized and therefore may contain harmful bacteria that can cause serious illness in children, the elderly, and persons with weakened immune systems.
• Must also list 16oz/473ml. I would also like to add my logo up at the top.
Nice to have
• Eye catching, not too many designs on the label.
• Maybe like the juice name and list of 3 benefits of the juice.
• I was thinking just all white for the design. I copied a pasted their rules on white. I’m not sure it applies here.
• White ink can be applied in many different ways to enhance your design. Including a white layer in your design will allow us to see where you want white ink to print. We suggest creating an individual file in your design labeled “White Layer” with a 100% Magenta fill for areas your design needs white ink printed.
• Images in documents should have a min 300dpi

```html
<!DOCTYPE html>
<html lang="en">
<head>
<meta charset="utf-8">
<title>Cold Pressed Juice – Tropical Label</title>
<link rel="stylesheet" href="https://fonts.googleapis.com/css2?family=Fira+Sans:wght@300;700;800;900&family=Roboto+Condensed:wght@700&display=swap">
<style>
  :root {
    --backdrop: #ababab;
    --ink-white: #ffffff;
    --fruit-red: #c8241c;
    --fruit-orange: #f08a1c;
    --fruit-yellow: #f6c646;
    --fruit-green: #9aa23a;
  }
  * { margin: 0; padding: 0; box-sizing: border-box; }
  html, body { width: 1200px; height: 900px; overflow: hidden; }
  body { background: var(--backdrop); color: var(--ink-white); font-family: "Fira Sans", Arial, sans-serif; }
  .label { position: relative; width: 1200px; height: 900px; }

  .logo-slot {
    position: absolute; left: 558px; top: 70px;
    font-weight: 300; font-size: 43px; line-height: 43px; letter-spacing: 0.5px;
  }
  .product-title { position: absolute; left: 498px; top: 217px; overflow: visible; }
  .flavour-name {
    position: absolute; left: 499px; top: 349px; width: 204px; height: 89px;
    border-radius: 36px 10px 36px 10px;
    background: linear-gradient(100deg, var(--fruit-orange) 0%, var(--fruit-red) 30%, var(--fruit-yellow) 55%, var(--fruit-orange) 75%, var(--fruit-green) 100%);
  }
  .description-rule {
    position: absolute; left: 506px; top: 488px; width: 5px; height: 94px; background: var(--ink-white);
  }
  .description {
    position: absolute; left: 523px; top: 486px;
    font-family: "Roboto Condensed", "Arial Narrow", sans-serif; font-weight: 700;
    font-size: 11px; line-height: 14.4px; white-space: nowrap;
  }
  .warning { position: absolute; left: 486px; top: 642px; }
  .volume {
    position: absolute; left: 556px; top: 761px;
    font-weight: 800; font-size: 14.5px; letter-spacing: 0.2px;
  }
</style>
</head>
<body>
  <main class="label">
    <div class="logo-slot">LOGO<br>HERE</div>

    <svg class="product-title" width="230" height="100" viewBox="0 0 230 100" aria-label="Cold Pressed Juice">
      <text x="-99" y="30" transform="rotate(-90)" fill="var(--ink-white)"
            font-family="Fira Sans, sans-serif" font-weight="300" font-size="40"
            textLength="99" lengthAdjust="spacingAndGlyphs">COLD</text>
      <text x="39" y="34" fill="var(--ink-white)"
            font-family="Fira Sans, sans-serif" font-weight="700" font-size="40"
            textLength="178" lengthAdjust="spacingAndGlyphs">PRESSED</text>
      <text x="41" y="97" fill="var(--ink-white)"
            font-family="Fira Sans, sans-serif" font-weight="900" font-size="70"
            textLength="166" lengthAdjust="spacingAndGlyphs">JUICE</text>
    </svg>

    <div class="flavour-name" role="img" aria-label="Hand-lettered flavour name 'Tropical' filled with a tropical fruit photo"></div>

    <div class="description-rule"></div>
    <p class="description">Lorem ipsum dolor sit amet,<br>consectetur adipiscing elit,<br>sed do eiusmod tempor<br>incididunt ut labore et<br>dolore magna aliqua. Quis<br>ipsum suspendisse ultrices<br>gravida. Risus commodo</p>

    <svg class="warning" width="226" height="83" viewBox="0 0 226 83" aria-label="WARNING: This product has not been pasteurized and therefore may contain harmful bacteria that can cause serious illness in children, the elderly, and persons with weakened immune systems.">
      <rect x="0.75" y="0.75" width="224.5" height="81.5" fill="none" stroke="var(--ink-white)" stroke-width="1.5"/>
      <g fill="var(--ink-white)" font-family="Fira Sans, sans-serif" font-weight="700" font-size="10.5">
        <text x="12" y="21" textLength="203" lengthAdjust="spacing">WARNING: This product has not been</text>
        <text x="12" y="33.5" textLength="203" lengthAdjust="spacing">pasteurized and therefore may contain</text>
        <text x="12" y="45.5" textLength="203" lengthAdjust="spacing">harmful bacteria that can cause serious</text>
        <text x="12" y="58" textLength="203" lengthAdjust="spacingAndGlyphs">illness in children, the elderly, and persons</text>
        <text x="113" y="70" text-anchor="middle" textLength="161" lengthAdjust="spacingAndGlyphs">with weakened immune systems.</text>
      </g>
    </svg>

    <p class="volume">16oz/473ml</p>
  </main>
</body>
</html>
```